Business Cards + Flyer + Letterhead for Care Recruitment Agency

We are a recruitment agency for the health & care sector. We need designs made for business cards, A5 double-sided flyer, and a letterhead template.

Our branding message is professionalism, care, compassion, expertise. We are experts in recruitment for the care & health industry.

Our logo source files and colours are here - https://www.fileporta.net/sh/qrvn82lopx4kdte/BBBgKy8LMQ27uTnPwZxHcVobsa?dl=0

For the business card, I have attached an example we like. We want a vertical business card design, something very similar to the example given. The design should match our logo in terms of brand colors. On one side should be our logo, our website (www.hollowmere.co.uk) and Care Recruitment Specialists written somewhere visible that fits, between our logo and the website at the bottom. On the other side should be our details.

Details on the front:

Logo with slogan
Care Recruitment Specialists
www.hollowmere.co.uk

Details on the back:

Tobias Orlund
Managing Director

Pellam House, 31-39 Larkfield St, Birmingham, B4 7QD
07612 495371
tobias@hollowmere.co.uk
www.hollowmere.co.uk

Marnie Holloway
Business Development Director

07831 204968
marnie@hollowmere.co.uk
www.hollowmere.co.uk

For the A5 flyer, I have attached some pictures we've used for the website, which could be used for the flyer as well. To get a better idea of our branding, please visit our website - https://hollowmere.co.uk/

The text for the flyer is also attached.

Finally, the letterhead template should be a docx template with our logo and our identifiable branding (the same shapes and matching colours you will come up with for the business cards and flyer).

```html
<!DOCTYPE html>
<html lang="en">
<head>
<meta charset="utf-8">
<title>Hollowmere Business Card</title>
<link href="https://fonts.googleapis.com/css2?family=Bebas+Neue&family=Poppins:wght@400;600&display=swap" rel="stylesheet">
<style>
  :root {
    --stage: #e6e7e9;
    --card: #f5f5f6;
    --navy: #0d2b66;
    --sky: #12b4ec;
    --text: #4a4a4a;
    --mark: #1a8cf0;
  }
  * { margin: 0; padding: 0; box-sizing: border-box; }
  html, body { width: 1200px; height: 1200px; overflow: hidden; }
  body {
    background: var(--stage);
    font-family: "Poppins", sans-serif;
    position: relative;
  }
  .card {
    position: absolute;
    top: 226px;
    width: 391px;
    height: 686px;
    background: var(--card);
    border-radius: 22px;
    text-align: center;
  }
  .card--details { left: 195px; }
  .card--brand { left: 660px; }

  .person-name {
    position: absolute; left: 0; right: 0; top: 228px;
    font-family: "Bebas Neue", sans-serif;
    font-size: 42px; line-height: 1; color: var(--navy);
    letter-spacing: 0.5px;
  }
  .person-role {
    position: absolute; left: 0; right: 0; top: 268px;
    font-size: 15.5px; color: var(--sky);
  }
  .contact-icons {
    position: absolute; left: 0; right: 0; top: 310px;
    display: flex; justify-content: center; align-items: center; gap: 4px;
  }
  .contact-icons .rule { width: 32px; height: 1.5px; background: var(--navy); margin: 0 8px; }
  .contact-icons svg { width: 19px; height: 19px; display: block; }
  .contact-list {
    position: absolute; left: 0; right: 0; top: 340px;
    list-style: none; font-size: 15.5px; line-height: 19.5px; color: var(--text);
  }
  .divider {
    position: absolute; left: 67px; width: 262px; top: 423px;
    height: 1.5px; background: var(--navy);
  }
  .address {
    position: absolute; left: 0; right: 0; top: 438px;
    font-size: 15.5px; line-height: 20px; color: var(--text); font-style: normal;
  }

  .brand-dot {
    position: absolute; left: 50%; top: 262px; width: 64px; height: 64px;
    margin-left: -32px; border-radius: 50%; background: var(--mark);
  }
  .brand-name {
    position: absolute; left: 0; right: 0; top: 366px;
    font-size: 31px; font-weight: 600; letter-spacing: 4px;
    color: var(--navy); line-height: 1;
  }
  .brand-tagline {
    position: absolute; left: 0; right: 0; top: 403px;
    font-size: 16px; color: var(--text);
  }
</style>
</head>
<body>
  <section class="card card--details">
    <h1 class="person-name">Marnie Holloway</h1>
    <p class="person-role">Business Development Director</p>
    <div class="contact-icons">
      <span class="rule"></span>
      <svg viewBox="0 0 20 20" aria-hidden="true">
        <circle cx="10" cy="10" r="10" fill="var(--navy)"/>
        <path d="M7 5.5l1.6 0 .8 2.3-1.1.9a6 6 0 0 0 3 3l.9-1.1 2.3.8 0 1.6c0 .6-.5 1-1.1 1A8 8 0 0 1 6 6.6c0-.6.4-1.1 1-1.1z" fill="#fff"/>
      </svg>
      <svg viewBox="0 0 20 20" aria-hidden="true">
        <circle cx="10" cy="10" r="10" fill="var(--navy)"/>
        <rect x="5" y="6.5" width="10" height="7" rx="1" fill="#fff"/>
        <path d="M5.5 7l4.5 3.5L14.5 7" fill="none" stroke="var(--navy)" stroke-width="1"/>
      </svg>
      <svg viewBox="0 0 20 20" aria-hidden="true">
        <circle cx="10" cy="10" r="10" fill="var(--navy)"/>
        <circle cx="10" cy="10" r="5" fill="none" stroke="#fff" stroke-width="1.3"/>
        <path d="M5 10h10M10 5c-2.2 2.8-2.2 7.2 0 10M10 5c2.2 2.8 2.2 7.2 0 10" fill="none" stroke="#fff" stroke-width="1"/>
      </svg>
      <span class="rule"></span>
    </div>
    <ul class="contact-list">
      <li>07831 204968</li>
      <li>marnie@hollowmere.co.uk</li>
      <li>www.hollowmere.co.uk</li>
    </ul>
    <div class="divider"></div>
    <address class="address">Pellam House, 31-39,<br>Larkfield St, Birmingham, B4 7QD</address>
  </section>

  <section class="card card--brand">
    <div class="brand-dot"></div>
    <h2 class="brand-name">HOLLOWMERE</h2>
    <p class="brand-tagline">Care Recruitment Specialists</p>
  </section>
</body>
</html>
```